Two (2) Merchant Advance Banner Ads

I need two (2) ads with rotating gif with 3 transitions for http://fundlinker.com/

Ad Specs:
Ad 1 must be an image equal to 250x250 pixels for website and email newsletter. .jpg, .gif, and
.png okay. No Flash!

Ad 2 must be an image equal to 720x90 pixels for website and mobile device view. .jpg, .gif, and
.png only. No Flash!

Client: Harwick Funding Partners merchant cash advance company out of Chicago. They provide alternative (to a bank loan) financing for small business owners across the U.S.
Here's their website: www.harwickfp.com

Purpose: Recruit 3rd party sellers of alternative financing. There are many sales financing professionals already out there soliciting small businesses, we want them to make a decision to sell Harwick's financing product to small businesses.

Copy:
Real People.
Competitive Commissions.
Great Rates.

I would like the logo (attached), phone number and CTA button to appear on all three transitions.
Call (888) 417-2859
Button: Get Started

Style:
Either something clean and simple, or something similar (not identifcal) to ads attached.
Brand standards guide is attached. Please use colors from guide.

```html
<!DOCTYPE html>
<html lang="en">
<head>
<meta charset="utf-8">
<title>Harwick Funding Partners – Banner Set</title>
<link rel="stylesheet" href="https://fonts.googleapis.com/css2?family=Bebas+Neue&family=Bree+Serif&family=Open+Sans:wght@600;700&display=swap">
<style>
  :root{
    --canvas:#ffffff;
    --ink:#000000;
    --slate:#525a74;
    --slate-dark:#3a3d48;
    --olive:#b4bf4c;
    --olive-light:#c8d066;
    --olive-dark:#98a43a;
    --orange:#e5761c;
    --orange-dark:#c85f10;
    --button-text:#4a3320;
    --white:#ffffff;
  }
  html,body{margin:0;padding:0;}
  body{
    width:1200px;height:1000px;overflow:hidden;
    background:var(--canvas);position:relative;
    font-family:"Open Sans",Arial,sans-serif;
  }
  .ad{position:absolute;border:1px solid var(--ink);overflow:hidden;background:var(--white);}

  .photo{
    position:absolute;
    background:linear-gradient(135deg,var(--olive-light) 0%,var(--olive) 45%,var(--olive-dark) 100%);
  }
  .headline{
    position:absolute;margin:0;
    font-family:"Bebas Neue",Impact,sans-serif;font-weight:400;
    color:var(--white);text-align:center;white-space:nowrap;
    text-shadow:3px 3px 0 var(--slate-dark);
  }
  .phone{
    position:absolute;margin:0;text-align:center;white-space:nowrap;
    font-family:"Bree Serif",Georgia,serif;color:var(--slate);
    text-shadow:-1px -1px 0 var(--white),1px -1px 0 var(--white),-1px 1px 0 var(--white),1px 1px 0 var(--white),2px 2px 0 var(--white);
  }
  .cta{
    position:absolute;width:118px;height:38px;box-sizing:border-box;
    background:var(--orange);border:1px solid var(--orange-dark);border-radius:3px;
    box-shadow:0 2px 2px rgba(0,0,0,.25);
    font-weight:700;font-size:14px;line-height:36px;text-align:center;
    color:var(--button-text);letter-spacing:-.2px;
  }
  .brand-name{
    position:absolute;margin:0;font-weight:600;color:var(--slate);line-height:1.1;
  }

  /* Square 250 */
  .ad-square{width:250px;height:250px;top:134px;}
  .ad-square .photo{left:0;top:0;width:250px;height:174px;}
  .ad-square .rule{position:absolute;left:0;top:174px;width:250px;height:4px;background:var(--slate);}
  .ad-square .headline{left:0;width:250px;}
  .ad-square .headline.tall{top:6px;font-size:78px;line-height:64px;}
  .ad-square .headline.wide{top:26px;font-size:50px;line-height:44px;}
  .ad-square .phone{left:0;width:250px;top:138px;font-size:23px;}
  .ad-square .brand-name{left:10px;top:196px;width:100px;font-size:14px;}
  .ad-square .cta{left:122px;top:196px;}

  /* Leaderboard 720x90 */
  .ad-wide{width:720px;height:90px;}
  .ad-wide .photo{left:150px;top:0;width:570px;height:90px;}
  .ad-wide .curve{position:absolute;left:0;top:0;}
  .ad-wide .brand-name{left:12px;top:24px;width:160px;font-size:17px;}
  .ad-wide .headline{left:188px;width:400px;top:0;font-size:66px;line-height:66px;}
  .ad-wide .headline.wide{font-size:44px;line-height:44px;top:13px;}
  .ad-wide .phone{left:188px;width:400px;top:61px;font-size:20px;}
  .ad-wide .cta{left:585px;top:27px;}
</style>
</head>
<body>

  <section class="ad ad-square" style="left:156px;">
    <div class="photo" role="img" aria-label="Team of people in an office meeting, tinted olive green"></div>
    <h2 class="headline tall">Real<br>People.</h2>
    <p class="phone">Call (888) 417-2859</p>
    <div class="rule"></div>
    <p class="brand-name">Harwick Funding Partners</p>
    <div class="cta">GET IN TOUCH</div>
  </section>

  <section class="ad ad-square" style="left:474px;">
    <div class="photo" role="img" aria-label="Team of people in an office meeting, tinted olive green"></div>
    <h2 class="headline wide">Competitive<br>Commissions.</h2>
    <p class="phone">Call (888) 417-2859</p>
    <div class="rule"></div>
    <p class="brand-name">Harwick Funding Partners</p>
    <div class="cta">GET IN TOUCH</div>
  </section>

  <section class="ad ad-square" style="left:791px;">
    <div class="photo" role="img" aria-label="Team of people in an office meeting, tinted olive green"></div>
    <h2 class="headline tall">Great<br>Rates.</h2>
    <p class="phone">Call (888) 417-2859</p>
    <div class="rule"></div>
    <p class="brand-name">Harwick Funding Partners</p>
    <div class="cta">GET IN TOUCH</div>
  </section>

  <section class="ad ad-wide" style="left:239px;top:477px;">
    <div class="photo" role="img" aria-label="Team of people in an office meeting, tinted olive green"></div>
    <svg class="curve" width="200" height="90" viewBox="0 0 200 90"><path d="M0 0H150Q186 45 150 90H0Z" fill="#fff" stroke="#525a74" stroke-width="4"/><rect x="0" y="0" width="4" height="90" fill="#fff"/></svg>
    <p class="brand-name">Harwick Funding Partners</p>
    <h2 class="headline">Real People.</h2>
    <p class="phone">Call (888) 417-2859</p>
    <div class="cta">GET IN TOUCH</div>
  </section>

  <section class="ad ad-wide" style="left:239px;top:633px;">
    <div class="photo" role="img" aria-label="Team of people in an office meeting, tinted olive green"></div>
    <svg class="curve" width="200" height="90" viewBox="0 0 200 90"><path d="M0 0H150Q186 45 150 90H0Z" fill="#fff" stroke="#525a74" stroke-width="4"/><rect x="0" y="0" width="4" height="90" fill="#fff"/></svg>
    <p class="brand-name">Harwick Funding Partners</p>
    <h2 class="headline wide">Competitive Commissions.</h2>
    <p class="phone">Call (888) 417-2859</p>
    <div class="cta">GET IN TOUCH</div>
  </section>

  <section class="ad ad-wide" style="left:237px;top:800px;">
    <div class="photo" role="img" aria-label="Team of people in an office meeting, tinted olive green"></div>
    <svg class="curve" width="200" height="90" viewBox="0 0 200 90"><path d="M0 0H150Q186 45 150 90H0Z" fill="#fff" stroke="#525a74" stroke-width="4"/><rect x="0" y="0" width="4" height="90" fill="#fff"/></svg>
    <p class="brand-name">Harwick Funding Partners</p>
    <h2 class="headline">Great Rates.</h2>
    <p class="phone">Call (888) 417-2859</p>
    <div class="cta">GET IN TOUCH</div>
  </section>

</body>
</html>
```